I need to redesign this website. Modern Fun Professional Redesign For www.GladPerksHub.com = New Name www.ClaimVouchly.com

Use existing content as it is on website exactly and we will revise after initial mock ups.

The new name will be ClaimVouchly.com please make a quick logo for this site too while redesigning.

Make it look like an official website....

Target Market(s)

Consumers that are redeeming certificates that businesses gave to them as a gift for customer loyalty,e tc.

Industry/Entity Type

It Professional

Logo Text

www.ClaimVouchly.com

Number of Pages Required

4 page

Colors

Designer to choose colors to be used in the design.

Requirements
Must have
• Must look professional, build trust and credibility.
Nice to have
• open
Should not have
• open

```html
<!DOCTYPE html>
<html lang="en">
<head>
<meta charset="utf-8">
<title>ClaimVouchly – Form &amp; Terms Module</title>
<link href="https://fonts.googleapis.com/css2?family=Cabin:wght@500;600;700&family=Open+Sans:wght@300;400;600&display=swap" rel="stylesheet">
<style>
  :root{
    --page:#ffffff;
    --ink:#1e1e1e;
    --ink-soft:#3a3a3a;
    --note:#3c3c3c;
    --module-grey:#8a8a8a;
    --green:#7aa818;
    --field-line:#a9a9a9;
    --hint:#8e8e8e;
    --button:#4fc1e3;
    --badge-top:#5aa7b8;
    --badge-bottom:#9ccbd4;
    --dot:#c9dcc0;
    --shade:#ececec;
  }
  *{box-sizing:border-box;margin:0;padding:0}
  html,body{width:1200px;height:598px;overflow:hidden;background:var(--page)}
  body{position:relative;font-family:"Open Sans",sans-serif;color:var(--ink)}
  .abs{position:absolute}
  .bottom-shade{left:0;top:536px;width:1200px;height:62px;background:linear-gradient(to bottom,var(--shade),#fff)}

  .module-title{left:0;width:240px;top:12px;text-align:center;font-family:"Cabin",sans-serif;font-weight:600;font-size:24px;line-height:32px;color:var(--module-grey);letter-spacing:.5px}
  .module-note{left:30px;top:102px;width:172px;font-family:"Cabin",sans-serif;font-weight:600;font-size:16px;line-height:22.7px;color:var(--note)}
  .side-note{left:993px;top:465px;width:170px;font-family:"Cabin",sans-serif;font-weight:600;font-size:16px;line-height:23px;color:var(--note)}

  .headline{left:0;width:1200px;top:6px;text-align:center;font-family:"Cabin",sans-serif;font-weight:700;font-size:24px;color:var(--green);letter-spacing:1px}
  .lead{left:0;width:1200px;top:62px;text-align:center;font-weight:300;font-size:22px;line-height:30px;color:var(--ink)}
  .instruction{left:0;width:1200px;top:133px;text-align:center;font-size:13px;color:var(--ink-soft)}

  .label{font-size:10.5px;color:var(--ink)}
  .field{border:1px solid var(--field-line);background:#fff}
  .callback{right:616px;top:349px;font-size:10.5px;display:flex;align-items:center;gap:4px}
  .callback .box{width:9px;height:9px;border:1px solid #777;border-radius:1px}

  .captcha{left:382px;top:421px;width:72px;height:27px;background:repeating-linear-gradient(45deg,#c7cfe0 0 2px,#e8ecf4 2px 4px);display:flex;align-items:center;justify-content:center;font-family:"Cabin",sans-serif;font-weight:700;font-size:17px;color:#4a5a8a;letter-spacing:1px}

  .questions-title{left:640px;top:182px;font-family:"Cabin",sans-serif;font-weight:600;font-size:17px}
  .questions-copy{left:639px;top:205px;width:340px;font-size:10px;line-height:17.5px}
  .counter{right:234px;top:290px;font-size:10px;color:var(--hint)}

  .submit{left:859px;top:419px;width:107px;height:30px;background:var(--button);border-radius:3px;display:flex;align-items:center;justify-content:center;font-family:"Cabin",sans-serif;font-weight:500;font-size:19px;color:var(--ink)}
  .terms-badge{left:891px;top:462px}

  .safelist{left:0;width:1200px;top:480px;text-align:center;font-size:7.5px;line-height:11px;color:#555}
  .safelist .faint{color:#888}
  .slide-dots{left:590px;top:512px;display:flex;gap:7px}
  .slide-dots span{width:5px;height:5px;border-radius:50%;background:var(--dot)}
</style>
</head>
<body>
  <div class="abs bottom-shade"></div>

  <div class="abs module-title">Module,<br>“FORM &amp; TERMS”</div>
  <p class="abs module-note">This is the form, which does not need much explana­tion however what if it is interesting, is that under the word submit there is a porpoise that says to see terms, when the client click there or in the menu a slide will be dis­played that Will present in the same area the terms of the business or cer­tificate.</p>

  <h1 class="abs headline">GET STARTED TODAY!</h1>
  <p class="abs lead">Submit Your Information Below And You Will Be Contacted<br>Within 1 Business Day.</p>
  <p class="abs instruction">You Must Fill In All Fields Below In Order For Us To Assist You. Incomplete information could result in no contact at all.</p>

  <span class="abs label" style="left:235px;top:170px">Name</span>
  <div class="abs field" style="left:234px;top:186px;width:352px;height:32px"></div>
  <span class="abs label" style="left:233px;top:231px">Certificate ID #:</span>
  <div class="abs field" style="left:234px;top:246px;width:352px;height:31px"></div>
  <span class="abs label" style="left:235px;top:289px">E-mail</span>
  <div class="abs field" style="left:234px;top:306px;width:352px;height:31px"></div>
  <span class="abs label" style="left:236px;top:349px">Phone:</span>
  <div class="abs callback">Yes call me&nbsp; back for more info <span class="box"></span></div>
  <div class="abs field" style="left:234px;top:366px;width:352px;height:31px"></div>

  <span class="abs label" style="left:236px;top:432px">Enter Security Code Above:</span>
  <div class="abs captcha">b2byb</div>
  <div class="abs field" style="left:486px;top:419px;width:98px;height:30px"></div>

  <h2 class="abs questions-title">Have Questions?</h2>
  <p class="abs questions-copy">We are here to help you redeem your certificates.<br>Feel free to contact us with any questions or suggestions on how we can do our job better</p>
  <span class="abs label" style="left:638px;top:290px">How May We Assist You?</span>
  <span class="abs counter">256&nbsp; characters left</span>
  <div class="abs field" style="left:638px;top:306px;width:328px;height:91px"></div>

  <div class="abs submit">Submit</div>

  <svg class="abs terms-badge" width="42" height="44" viewBox="0 0 42 44" aria-label="See our terms">
    <defs>
      <linearGradient id="badgeFill" x1="0" y1="0" x2="0" y2="1">
        <stop offset="0" stop-color="var(--badge-top)"/>
        <stop offset="1" stop-color="var(--badge-bottom)"/>
      </linearGradient>
    </defs>
    <path d="M1 2 Q21 -2 41 2 V18 Q41 36 21 43 Q1 36 1 18 Z" fill="url(#badgeFill)"/>
    <text x="21" y="16" text-anchor="middle" font-family="Cabin,sans-serif" font-weight="700" font-size="6" fill="#fff">SEE OUR</text>
    <text x="21" y="23" text-anchor="middle" font-family="Cabin,sans-serif" font-weight="700" font-size="6" fill="#fff">TERMS</text>
  </svg>

  <svg class="abs" style="left:938px;top:469px" width="46" height="10" viewBox="0 0 46 10" aria-hidden="true">
    <line x1="6" y1="5" x2="44" y2="5" stroke="#333" stroke-width="1"/>
    <path d="M1 5 L8 1.5 L8 8.5 Z" fill="#333"/>
  </svg>
  <p class="abs side-note">The client will click here and the module will be dis­played terms</p>

  <p class="abs safelist">Please add DoNotReply@ClaimVouchly.com to your email safelist as this can help assure that you will receive our email response.<br><span class="faint">Please note that that our emails could be sent to your junk or spam folders so please check there.</span></p>
  <div class="abs slide-dots"><span></span><span></span></div>
</body>
</html>
```